FOOD DELIVERY BRAND NEEDS WEBSITE TO GET SUBSCRIBERS

web design needed for a food delivery brand/label,
website should display who we are, how it works and push futur clients to get the label for an online application. Should look serious/official, trustworthy and confident. colors are black and gold like logo

Target Market(s)

restaurants

Industry/Entity Type

restaurant

Number of Pages Required

4 page

Requirements
Must have
• home page, who we are, our partners, subscribe, 2 subscribe button : 1 on top 1 bottom
Nice to have
• a graphic showing average + 15% sales thanks the label

```html
<!DOCTYPE html>
<html lang="en">
<head>
<meta charset="utf-8">
<title>Gilded Route Seal — Good Delivery Good Food</title>
<link rel="stylesheet" href="https://fonts.googleapis.com/css2?family=Montserrat:wght@400;500;600;700&display=swap">
<style>
  :root {
    --gold: #d4ab3a;
    --gold-deep: #c99f2e;
    --ink: #0a0c0b;
    --ink-soft: #151716;
    --white: #ffffff;
    --card-text: #3a3a3a;
  }
  * { margin: 0; padding: 0; box-sizing: border-box; }
  html, body { width: 1200px; height: 3047px; overflow: hidden; }
  body {
    position: relative;
    background: var(--ink);
    color: var(--white);
    font-family: "Montserrat", Arial, sans-serif;
  }
  .abs { position: absolute; }

  /* Hero */
  .hero {
    position: absolute; left: 0; top: 0; width: 1200px; height: 657px;
    background:
      radial-gradient(ellipse at 50% 45%, rgba(60,56,48,.55), rgba(10,10,10,0) 60%),
      linear-gradient(180deg, #1b1a18 0%, #2a2824 45%, #3a3630 75%, #24221f 100%);
  }
  .nav-link { position: absolute; top: 46px; font-size: 14px; font-weight: 600; color: var(--white); text-decoration: none; }
  .nav-link.is-active { border-bottom: 2px solid var(--gold); padding-bottom: 4px; }
  .brand { position: absolute; left: 450px; top: 40px; width: 300px; text-align: center; }
  .brand-mark { width: 46px; height: 46px; margin: 0 auto 10px; background: var(--gold); border-radius: 50%; }
  .brand-name { font-size: 17px; font-weight: 500; color: var(--gold); letter-spacing: 1px; text-transform: uppercase; line-height: 1.15; }
  .hero-kicker { position: absolute; left: 0; width: 1200px; top: 262px; text-align: center; font-size: 14px; font-weight: 500; color: var(--gold); }
  .hero-title { position: absolute; left: 0; width: 1200px; top: 288px; text-align: center; font-size: 48px; font-weight: 600; letter-spacing: .5px; }
  .hero-text { position: absolute; left: 400px; width: 400px; top: 352px; text-align: center; font-size: 14px; font-weight: 500; line-height: 21px; }
  .btn { position: absolute; display: flex; align-items: center; justify-content: center; font-size: 13px; text-decoration: none; }
  .btn-gold { background: var(--gold); color: #2a2208; font-weight: 500; letter-spacing: .5px; }
  .btn-outline { border: 1px solid var(--white); color: var(--white); font-weight: 600; }

  /* How it works */
  .section-title { position: absolute; font-size: 31px; font-weight: 600; color: var(--gold); }
  .body-text { font-size: 14px; font-weight: 500; line-height: 21.3px; }
  .rule { position: absolute; left: 111px; top: 963px; width: 34px; height: 2px; background: var(--gold); }
  .checklist { position: absolute; left: 111px; top: 978px; list-style: none; }
  .checklist li { display: flex; align-items: center; height: 35.5px; font-size: 14px; font-weight: 500; }
  .checklist svg { margin-right: 17px; }
  .photo-courier {
    position: absolute; left: 609px; top: 728px; width: 409px; height: 355px;
    background: radial-gradient(ellipse at 45% 55%, #b89468 0%, #5a4632 35%, #1b1b1b 70%, rgba(10,12,11,0) 100%);
  }
  .dot { position: absolute; left: 844px; top: 1099px; width: 6px; height: 6px; border-radius: 50%; background: var(--gold); }

  /* Who we are */
  .plate-ring { position: absolute; left: 142px; top: 1320px; width: 320px; height: 320px; border-radius: 50%; background: var(--gold); }
  .plate-photo {
    position: absolute; left: 204px; top: 1382px; width: 196px; height: 196px; border-radius: 50%;
    background: radial-gradient(circle, #6a3a22 0%, #3d4a24 45%, #141a1c 80%);
  }

  /* Partners */
  .center { position: absolute; left: 0; width: 1200px; text-align: center; }
  .partner { position: absolute; top: 1868px; width: 285px; text-align: center; font-size: 52px; font-weight: 600; color: var(--white); letter-spacing: -1px; }

  /* Testimonials */
  .quote-card { position: absolute; top: 2177px; width: 308px; height: 166px; background: var(--white); padding: 20px 26px; font-size: 12.5px; line-height: 21.3px; color: var(--card-text); }
  .quote-card::after { content: ""; position: absolute; left: 30px; bottom: -14px; border: 9px solid transparent; border-top: 14px solid var(--white); border-bottom: 0; }
  .avatar { position: absolute; top: 2372px; width: 44px; height: 44px; border-radius: 50%; background: linear-gradient(135deg, #4a5358, #1e2326); }
  .client-name { position: absolute; top: 2377px; font-size: 12.5px; font-weight: 600; }
  .client-role { position: absolute; top: 2398px; font-size: 12.5px; color: var(--gold); }

  /* Call to action */
  .cta {
    position: absolute; left: 0; top: 2452px; width: 1200px; height: 424px;
    background: radial-gradient(ellipse at 75% 20%, #3a302a 0%, #1b1815 40%, #0f100e 100%);
  }

  /* Footer */
  .footer { position: absolute; left: 0; top: 2876px; width: 1200px; height: 171px; background: var(--gold); }
  .footer-col { position: absolute; top: 20px; }
  .footer-col h4 { font-size: 16px; font-weight: 600; margin-bottom: 14px; }
  .footer-col a { display: block; font-size: 16px; color: var(--white); text-decoration: none; line-height: 31px; }
</style>
</head>
<body>

<header class="hero" role="img" aria-label="Dimly lit restaurant dining room with tables and chairs">
</header>
<nav>
  <a class="nav-link is-active" href="#" style="left:200px">Home</a>
  <a class="nav-link" href="#how" style="left:334px">How it Works</a>
  <a class="nav-link" href="#about" style="left:840px">About Us</a>
  <a class="nav-link" href="#contact" style="left:995px">Contact</a>
</nav>
<div class="brand">
  <div class="brand-mark"></div>
  <div class="brand-name">Gilded Route<br>Seal</div>
</div>
<p class="hero-kicker">Welcome to GILDED ROUTE SEAL</p>
<h1 class="hero-title">GOOD DELIVERY GOOD FOOD</h1>
<p class="hero-text">Lorem ipsum dolor sit amet, consectetuer adipiscing elit. Aenean commodo ligula eget dolor. Aenean</p>
<a class="btn btn-gold" href="#" style="left:477px;top:426px;width:114px;height:34px">SUBSCRIBE</a>
<a class="btn btn-outline" href="#" style="left:609px;top:426px;width:114px;height:34px">Learn More</a>

<section id="how">
  <h2 class="section-title" style="left:110px;top:806px">How it Works</h2>
  <p class="body-text abs" style="left:111px;top:889px;width:420px">Lorem ipsum dolor sit amet, consectetuer adipiscing elit. Aenean commodo ligula eget dolor. Aenean massa. Cum sociis natoque penatibus et magnis dis parturient montes,</p>
  <div class="rule"></div>
  <ul class="checklist">
    <li><svg width="22" height="16" viewBox="0 0 22 16"><path d="M2 8 L8 14 L20 2" fill="none" stroke="#d4ab3a" stroke-width="3.5" stroke-linecap="round" stroke-linejoin="round"/></svg>Lorem ipsum dolor sit amet,</li>
    <li><svg width="22" height="16" viewBox="0 0 22 16"><path d="M2 8 L8 14 L20 2" fill="none" stroke="#d4ab3a" stroke-width="3.5" stroke-linecap="round" stroke-linejoin="round"/></svg>Lorem ipsum dolor sit amet, consectetuer</li>
    <li><svg width="22" height="16" viewBox="0 0 22 16"><path d="M2 8 L8 14 L20 2" fill="none" stroke="#d4ab3a" stroke-width="3.5" stroke-linecap="round" stroke-linejoin="round"/></svg>Lorem ipsum dolor sit amet, consectetuer adipiscing</li>
  </ul>
  <div class="photo-courier" role="img" aria-label="Masked delivery courier in gloves holding out a paper food bag"></div>
  <div class="dot"></div>
</section>

<section id="about">
  <div class="plate-ring"></div>
  <div class="plate-photo" role="img" aria-label="Plate of glazed chicken wings with fresh greens"></div>
  <h2 class="section-title" style="right:114px;top:1338px">Who We Are</h2>
  <p class="body-text abs" style="left:558px;top:1403px;width:531px;text-align:right">Lorem ipsum dolor sit amet, consectetuer adipiscing elit. Aenean commodo ligula eget dolor. Aenean massa. Cum sociis natoque penatibus et magnis dis parturient montes, nascetur ridiculus mus. Donec quam felis, ultricies nec, pellentesque eu, pretium quis, sem. Nulla consequat massa quis enim. Donec pede justo, fringilla vel, aliquet nec, vulputate eget, arcu. In enim justo, rhoncus ut, imperdiet a, venenatis vitae, justo. Nullam dictum felis eu pede mollis pretium. Integer tincidunt. Cras dapibus. Vivamus</p>
</section>

<section id="partners">
  <h2 class="center" style="top:1744px;font-size:33px;font-weight:600">Partners</h2>
  <p class="center" style="top:1802px;font-size:14px;font-weight:500;color:var(--gold)">Lorem ipsum dolor sit amet, consectetuer adipiscing elit.</p>
  <div class="partner" style="left:110px">Forkline Go</div>
  <div class="partner" style="left:456px">Forkline Go</div>
  <div class="partner" style="left:802px">Forkline Go</div>
</section>

<section id="testimonials">
  <h2 class="center" style="top:2065px;font-size:35px;font-weight:600;color:var(--gold)">Testimonial</h2>
  <p class="center" style="top:2123px;font-size:14px;font-weight:500">What People Say about Us</p>

  <blockquote class="quote-card" style="left:112px">Lorem ipsum dolor sit amet, consectetuer adipiscing elit. Aenean commodo ligula eget dolor. Aenean massa. Cum sociis natoque penatibus et magnis dis parturient montes. Nascetur ridiculus mus. Donec quam</blockquote>
  <blockquote class="quote-card" style="left:446px">Aenean commodo ligula eget dolor. Aenean massa. Cum sociis natoque penatibus et magnis dis parturient montes.<br>Nascetur ridiculus mus. Donec quam felis, ultricies nec.</blockquote>
  <blockquote class="quote-card" style="left:781px">Aenean commodo ligula eget dolor. Aenean massa. Cum sociis natoque penatibus et magnis dis parturient montes.<br>Nascetur ridiculus mus. Donec quam felis, ultricies nec.</blockquote>

  <div class="avatar" style="left:129px" role="img" aria-label="Client portrait"></div>
  <span class="client-name" style="left:191px">John Smith</span>
  <span class="client-role" style="left:191px">Assistant Manager</span>

  <div class="avatar" style="left:463px" role="img" aria-label="Client portrait"></div>
  <span class="client-name" style="left:525px">Client name</span>
  <span class="client-role" style="left:525px">Software Developer</span>

  <div class="avatar" style="left:798px" role="img" aria-label="Client portrait"></div>
  <span class="client-name" style="left:860px">Client name</span>
  <span class="client-role" style="left:860px">Fitness Trainer</span>
</section>

<section class="cta" role="img" aria-label="Woman enjoying a meal in a warmly lit restaurant at night"></section>
<h2 class="center" style="top:2567px;font-size:33px;font-weight:600;line-height:38px">Want to get all these<br>conveniences?</h2>
<p class="center" style="top:2657px;font-size:14px;font-weight:500">Subscribe Now</p>
<a class="btn btn-gold" href="#" style="left:502px;top:2693px;width:196px;height:36px;font-size:12px;font-weight:700;color:var(--white)">SUBSCRIBE</a>

<footer class="footer" id="contact">
  <div class="footer-col" style="left:111px">
    <h4>Mobile app</h4>
    <a href="#">Features</a><a href="#">Live share</a><a href="#">Video record</a>
  </div>
  <div class="footer-col" style="left:396px">
    <h4>Community</h4>
    <a href="#">Featured artists</a><a href="#">The Portal</a><a href="#">Live events</a>
  </div>
  <div class="footer-col" style="left:680px">
    <h4>Company</h4>
    <a href="#">About us</a><a href="#">Contact us</a><a href="#">History</a>
  </div>
</footer>

</body>
</html>
```